Real Estate Valuation Services

format
A5 portrait, look at the picture
Double-sided: Front = visual & emotional, Back = informative & structured.
goal
Highlight the free hedonic property valuation as the main offer.
Build trust by presenting the company as an exclusive, family-owned real estate firm with local roots in Meilen/ZH.
Communicate the USP “Everything from one source” clearly – from valuation to notary support and tax guidance.
Target audience
Homeowners in the Lake Zurich region considering selling their property.
Clients who value exclusivity, professionalism, and personal service.
Design style
Modern, clean, elegant – plenty of white space. Look at the website: https://brunnhofwohnen.ch/
Tone: Professional, trustworthy, exclusive – not like a mass-market flyer.
If possible, the text should be in German. Contact details must be included:
info@brunnhofwohnen.ch
+41 77 562 18 04
Target Market(s)
property owner
Industry/Entity Type
real estate
Look and feel

```html
<!DOCTYPE html>
<html lang="de">
<head>
<meta charset="utf-8">
<title>Brunnhof Immobilien – Flyer</title>
<link href="https://fonts.googleapis.com/css2?family=Montserrat:ital,wght@0,500;0,600;0,700;0,800;1,600;1,700&family=Lato:wght@400;700&display=swap" rel="stylesheet">
<style>
  :root{
    --canvas:#f7f7f7;
    --paper:#ffffff;
    --ink:#1b1b1b;
    --text:#2a2a2a;
    --green:#2f9a52;
    --green-dark:#1d8a4e;
    --green-light:#7dbb42;
    --green-mist:#cfe6d2;
    --card-line:#e3e3e3;
  }
  *{box-sizing:border-box;margin:0;padding:0}
  html,body{width:1200px;height:1137px;overflow:hidden}
  body{background:var(--canvas);position:relative;font-family:"Lato",Arial,sans-serif;color:var(--text)}

  .page{position:absolute;top:204px;width:522px;height:735px;background:var(--paper);overflow:hidden;box-shadow:0 2px 10px rgba(0,0,0,.12)}
  .page--front{left:65px}
  .page--back{left:614px}

  .brand{display:flex;flex-direction:column;align-items:center;font-family:"Montserrat",Arial,sans-serif;color:var(--green);font-weight:700;line-height:1}
  .brand__name{font-size:42px;letter-spacing:-.5px}
  .brand__sub{font-size:17px;letter-spacing:2px;margin-top:6px}

  /* Front */
  .page--front .brand{position:absolute;top:40px;left:0;right:0}
  .headline{position:absolute;top:140px;left:0;right:0;text-align:center;font-family:"Montserrat",Arial,sans-serif;font-weight:800;font-size:38px;line-height:46px;color:var(--ink)}
  .front-rule{position:absolute;top:243px;left:49px;right:41px;height:1px;background:linear-gradient(90deg,var(--green-dark),var(--green-light))}
  .front-claim{position:absolute;top:260px;left:0;right:0;text-align:center;font-family:"Montserrat",Arial,sans-serif;font-style:italic;font-weight:700;font-size:19.5px;line-height:29px;color:var(--green-light)}
  .scenery{position:absolute;left:0;right:0;top:380px;bottom:0;background:linear-gradient(180deg,rgba(255,255,255,0) 0%,#e6ece6 20%,#b9d6bd 50%,#5fb26f 80%,#2f9a52 100%)}
  .portrait{position:absolute;left:8px;bottom:0;width:355px;height:362px;background:linear-gradient(180deg,#cfcfcf 0%,#9a9a9a 55%,#3a3a3a 100%);border-radius:150px 150px 0 0}

  /* Back */
  .hero-photo{position:absolute;top:0;left:0;right:0;height:205px;background:linear-gradient(180deg,#4a8fd6 0%,#9cc6ea 35%,#b9c7b5 60%,#e7eee7 85%,#ffffff 100%)}
  .offer{position:absolute;top:204px;left:27px;width:465px;height:175px;border:1.5px solid var(--green);background:var(--paper);padding:14px 38px 0}
  .offer__title{font-family:"Montserrat",Arial,sans-serif;font-weight:700;font-size:19.5px;color:var(--green-light);text-align:center;line-height:24px}
  .offer__sub{font-family:"Montserrat",Arial,sans-serif;font-weight:600;font-size:17px;color:var(--green-dark);text-align:center;line-height:22px}
  .offer__rule{height:1px;margin:8px 0 10px;background:linear-gradient(90deg,var(--green-dark),var(--green-light))}
  .offer__text{font-size:13.6px;line-height:17.5px;text-align:justify;color:var(--text)}

  .services{position:absolute;top:402px;left:29px;display:flex;gap:11px}
  .service{width:147px;height:152px;border:1px solid var(--card-line);box-shadow:0 1px 3px rgba(0,0,0,.08);text-align:center;padding-top:14px;position:relative}
  .service__title{font-family:"Montserrat",Arial,sans-serif;font-weight:700;font-size:17px;color:var(--green-dark)}
  .service__text{font-size:12.2px;line-height:15px;margin-top:6px;color:var(--text)}
  .service__icon{position:absolute;right:14px;bottom:10px;width:42px;height:42px}

  .cta{position:absolute;top:581px;left:35px;width:456px;height:67px;background:linear-gradient(90deg,var(--green-dark),var(--green-light));color:#fff;font-family:"Montserrat",Arial,sans-serif;font-weight:700;font-size:15px;line-height:21px;text-align:center;display:flex;align-items:center;justify-content:center;letter-spacing:.3px}

  .page--back .brand{position:absolute;top:662px;left:58px}
  .page--back .brand__name{font-size:30px}
  .page--back .brand__sub{font-size:13px;margin-top:5px}
  .contact{position:absolute;top:667px;left:264px;list-style:none;font-size:13.6px;line-height:17.5px;color:var(--text)}
  .contact li{display:flex;align-items:center;gap:7px}
  .contact svg{width:10px;height:10px;flex:none}
</style>
</head>
<body>

<section class="page page--front">
  <div class="brand"><span class="brand__name">Brunnhof</span><span class="brand__sub">IMMOBILIEN</span></div>
  <h1 class="headline">Ihre Immobilie.<br>Unser Versprechen.</h1>
  <div class="front-rule"></div>
  <p class="front-claim">„Kostenlose und exklusive<br>Immobilienbewertung am Zürichsee.“</p>
  <div class="scenery" role="img" aria-label="Landschaft am Zürichsee mit Bergen im Hintergrund, grün eingefärbt"></div>
  <div class="portrait" role="img" aria-label="Schwarz-Weiss-Porträt der Beraterin"></div>
</section>

<section class="page page--back">
  <div class="hero-photo" role="img" aria-label="Balkon mit Seeblick über Wohnhäuser am Zürichsee"></div>

  <div class="offer">
    <h2 class="offer__title">Kostenlose Immobilienbewertung</h2>
    <p class="offer__sub">exklusiv für Eigentümer am Zürichsee</p>
    <div class="offer__rule"></div>
    <p class="offer__text">„Wir sind ein familiengeführtes Immobilienunternehmen aus Meilen. Mit persönlicher Betreuung und diskretem Service begleiten wir Sie – von der ersten Bewertung bis hin zu Notar- und Steuerfragen.“</p>
  </div>

  <div class="services">
    <div class="service">
      <h3 class="service__title">Bewertung</h3>
      <p class="service__text">Marktgerechte<br>Wertermittlung</p>
      <svg class="service__icon" viewBox="0 0 42 42" fill="none" stroke="var(--green-dark)" stroke-width="2.4" stroke-linejoin="round">
        <path d="M4 20 L19 7 L34 20"/><path d="M8 17 V35 H22"/><circle cx="28" cy="29" r="6"/><path d="M32.5 33.5 L38 39"/>
      </svg>
    </div>
    <div class="service">
      <h3 class="service__title">Verkauf</h3>
      <p class="service__text">Exklusive<br>Vermarktung<br>&amp; Beratung</p>
      <svg class="service__icon" viewBox="0 0 42 42" fill="none" stroke="var(--green-dark)" stroke-width="2.4" stroke-linejoin="round">
        <rect x="14" y="5" width="14" height="22" rx="2" transform="rotate(20 21 16)"/><path d="M4 24 L12 22 L22 28 L30 28 L30 32 L20 32"/><path d="M4 36 L14 36 L24 38 L36 30"/>
      </svg>
    </div>
    <div class="service">
      <h3 class="service__title">Begleitung</h3>
      <p class="service__text">Alles aus einer Hand:<br>Notar &amp; Steuer</p>
      <svg class="service__icon" viewBox="0 0 42 42" fill="none" stroke="var(--green-dark)" stroke-width="2.4" stroke-linecap="round">
        <circle cx="21" cy="18" r="6"/><path d="M21 5v4M21 27v4M8 18h4M30 18h4M12 9l3 3M27 24l3 3M30 9l-3 3M12 27l3-3"/><path d="M6 38 L18 28M36 38 L24 28"/>
      </svg>
    </div>
  </div>

  <div class="cta">„FORDERN SIE JETZT IHRE KOSTENLOSE<br>IMMOBILIENBEWERTUNG AN!“</div>

  <div class="brand"><span class="brand__name">Brunnhof</span><span class="brand__sub">IMMOBILIEN</span></div>
  <ul class="contact">
    <li><svg viewBox="0 0 10 10"><rect x="0.5" y="1.5" width="9" height="7" fill="var(--green)"/><path d="M0.5 2 L5 5.5 L9.5 2" stroke="#fff" fill="none" stroke-width="1"/></svg>info@brunnhofwohnen.ch</li>
    <li><svg viewBox="0 0 10 10"><path d="M2 1 L4 1 L4.5 3.5 L3.3 4.3 Q4.5 6.5 5.7 6.7 L6.5 5.5 L9 6 L9 8 Q5 9.5 1 3 Z" fill="var(--green)"/></svg>+41 77 562 18 04</li>
    <li><svg viewBox="0 0 10 10"><circle cx="5" cy="5" r="4" fill="var(--green)"/></svg>brunnhofwohnen.ch</li>
  </ul>
</section>

</body>
</html>
```